Letterhead in Word Format

We are a small law firm in the Midwest. Our clientele is generally small business owners and companies.

We recently had a complete re-brand with a new logo, new letterhead, business cards, etc. However, the major issue now is that we cannot use the letterhead without physically ordering letterhead. Thus, invoices, and other items cannot be custom drafted.

We require custom letterhead in MICROSOFT WORD format. Our logo will be provided to you. And we will also provide a copy of the letterhead that was prepared.

We would like to see designs that are black and white, sophisticated, elegant, and generally professional. We prefer a traditional design with just a touch of contemporary.

Please do not submit any designs that are not Microsoft Word compatible.

EDIT: Please view the attached letterhead. The design must include the logo, name, address, fax, phone, email, and name of attorney.
Updates

Thank you all for submitting designs. I just wanted to quickly provide some feedback. I saw a few designs that had the logo at the bottom. Because there will be text with margins at 1" all around, it's not practical have the logo at the bottom. Also, designs with blocks of gray or black would cause our printer to bleed black onto the letterhead, so that is not practical as well.

If you have any comments, please feel free to leave me a message. Thank you.

Target Market(s)

Small business owners, companies, real estate investors and developers.

Industry/Entity Type

Small Business

Font styles to use
Script

Requirements
Must have
• Microsoft Word Format

```html
<!DOCTYPE html>
<html lang="en">
<head>
<meta charset="utf-8">
<title>The MRH Law Firm — Letterhead</title>
<link rel="stylesheet" href="https://fonts.googleapis.com/css2?family=EB+Garamond:wght@400;700&display=swap">
<style>
  :root {
    --paper: #ffffff;
    --ink: #222222;
    --firm-grey: #3a3a3a;
    --rule-grey: #c9c9c9;
    --ornament-grey: #d4d4d4;
    --footer-rule: #c4c4c4;
  }
  html, body {
    margin: 0;
    padding: 0;
    overflow: hidden;
    background: var(--paper);
  }
  .letterhead {
    position: relative;
    width: 916px;
    height: 1200px;
    background: var(--paper);
    overflow: hidden;
    font-family: "EB Garamond", Garamond, serif;
    color: var(--ink);
  }
  .firm-name {
    position: absolute;
    left: 37px;
    top: 82px;
    margin: 0;
    font-size: 23px;
    font-weight: 400;
    letter-spacing: 0.3px;
    color: var(--firm-grey);
    white-space: nowrap;
  }
  .header-rules {
    position: absolute;
    left: 292px;
    top: 96px;
    width: 574px;
    height: 22px;
  }
  .header-ornament {
    position: absolute;
    left: 683px;
    top: 89px;
    width: 36px;
    height: 46px;
  }
  .attorney {
    position: absolute;
    left: 720px;
    top: 52px;
  }
  .attorney-title {
    margin: 0;
    font-size: 10px;
    line-height: 12px;
  }
  .attorney-name {
    margin: 2px 0 0;
    font-size: 21px;
    font-weight: 700;
    letter-spacing: 0.4px;
    line-height: 24px;
    white-space: nowrap;
  }
  .footer-rule {
    position: absolute;
    left: 40px;
    top: 1141px;
    width: 838px;
    height: 3px;
    background: var(--footer-rule);
  }
  .contact {
    position: absolute;
    left: 0;
    top: 1149px;
    width: 916px;
    margin: 0;
    text-align: center;
    font-size: 13px;
    line-height: 19px;
    font-style: normal;
  }
  .contact span { margin: 0 9px; }
</style>
</head>
<body>
  <div class="letterhead">
    <header>
      <h1 class="firm-name">THE MRH LAW FIRM</h1>

      <svg class="header-rules" viewBox="0 0 574 22" aria-hidden="true">
        <g stroke="var(--rule-grey)" stroke-width="1.6">
          <line x1="0" y1="3" x2="574" y2="3"/>
          <line x1="0" y1="7.5" x2="574" y2="7.5"/>
          <line x1="0" y1="12" x2="574" y2="12"/>
          <line x1="0" y1="16.5" x2="574" y2="16.5"/>
          <line x1="0" y1="21" x2="574" y2="21"/>
        </g>
      </svg>

      <svg class="header-ornament" viewBox="0 0 36 46" role="img" aria-label="Decorative diamond ornament on the header rules">
        <rect width="36" height="46" fill="var(--ornament-grey)"/>
      </svg>

      <div class="attorney">
        <p class="attorney-title">Principal Attorney</p>
        <p class="attorney-name">DORIAN V. HALE</p>
      </div>
    </header>

    <footer>
      <div class="footer-rule"></div>
      <address class="contact">
        <span>Address: 2845 W. Alder Rd.&nbsp;&nbsp;&nbsp; Brookhaven, Illinois 60199</span><span>Phone: (708) 555-0142</span><span>Fax: (708) 555-0143</span><br>
        <span>Web: www.themrhlawfirm.com</span><span>Email: mrh@themrhlawfirm.com</span>
      </address>
    </footer>
  </div>
</body>
</html>
```